TKRVantage Website Design
New website
TKRVantage Website Design - Sports
Creative Brief
Sports
www.brisk-competitors.example (will be changing doman name)
We provide cutting edge sports performance training - speed/agility/conditioning for amateur and professional athletes. We use the latest in technology and techniques to teach the fundamentals of athleticisim. All athletes in all sports. Been in business for over 12 years. Co owners are athletes themselves with a passion for coaching/helping others achieve their athletic goals.
Dislikes: when it runs slow, not user friendly, not flexible design for changes/adding content Likes: easy/clear messaging for clients, self service for registration/payment, reflect business, modern design
Black
Silver (see logo)
Orange (see logo)
below header
www.quillrunperf.example/sandiego
www.motionworkshopkit.example
www.brantfieldtrainingcentre.example
Want to drive people to site and leverage the site for self service with our programs. Also drive to our ClipVista videos that demo. Want site to have video capability. Want to reflect calendaring/real time scheduling.

```html
<!DOCTYPE html>
<html lang="en">
<head>
<meta charset="utf-8">
<title>TKRVantage — Sports Performance Training</title>
<link rel="stylesheet" href="https://fonts.googleapis.com/css2?family=Open+Sans:ital,wght@0,400;0,600;0,700;0,800;1,700;1,800&display=swap">
<style>
:root{
  --page:#141414;
  --panel:#1f1f1f;
  --hero:#050505;
  --orange:#f07a1a;
  --orange-dark:#c95a08;
  --silver-light:#e9e9e9;
  --silver:#b9b9b9;
  --silver-dark:#8d8d8d;
  --text:#cfcfcf;
  --muted:#8a8a8a;
  --white:#ffffff;
  --line:#3a3a3a;
}
*{box-sizing:border-box;margin:0;padding:0}
html,body{width:1200px;height:1030px;overflow:hidden}
body{background:var(--page);font-family:"Open Sans",Arial,sans-serif;color:var(--text);position:relative}
.abs{position:absolute}

/* header */
.top-accent{left:700px;top:0;width:273px;height:4px;background:var(--orange)}
.utility-links{left:722px;top:8px;font-size:8px;color:var(--muted);word-spacing:3px}
.utility-links b{color:var(--white);font-weight:600}
.brand{left:240px;top:30px;display:flex;align-items:center;gap:10px}
.brand-dot{width:34px;height:34px;border-radius:50%;background:var(--orange)}
.brand-name{font-size:24px;font-weight:800;color:var(--silver-light);letter-spacing:.5px;white-space:nowrap}
.social{left:742px;top:44px;display:flex;gap:6px}
.social span{width:18px;height:18px;background:#3c3c3c;border:1px solid #555;border-radius:2px}
.search{left:858px;top:42px;width:112px;height:21px;background:#2a2a2a;border:1px solid #4a4a4a;border-radius:11px;font-size:9px;color:var(--muted);padding:4px 10px}
.search svg{position:absolute;right:7px;top:4px}

/* nav */
.main-nav{left:228px;top:96px;width:745px;height:22px;background:linear-gradient(#f2f2f2,var(--silver) 55%,var(--silver-dark));display:flex;align-items:stretch}
.main-nav a{flex:1;text-align:center;font-size:9.5px;font-weight:700;color:#333;text-decoration:none;line-height:22px;text-transform:uppercase}
.main-nav a.active{background:linear-gradient(#3a3a3a,#111);color:var(--white);font-size:11px}

/* hero */
.hero{left:228px;top:120px;width:745px;height:282px;background:var(--hero)}
.hero-title{left:345px;top:190px;font-size:30px;font-style:italic;font-weight:800;color:var(--white);line-height:38px;letter-spacing:-.3px;white-space:nowrap}
.hero-title .quote{font-size:46px;vertical-align:-8px;margin-right:6px}
.hero-title .line2{display:block;margin-left:-55px}
.hero-title em{color:var(--orange)}
.hero-sub{left:345px;top:290px;font-size:10px;color:#bdbdbd}
.hero-photo{left:715px;top:122px;width:190px;height:278px;background:radial-gradient(ellipse at 50% 45%,#5a6a86 0%,#26324a 45%,#050505 80%)}
.hero-arrow{top:250px}
.hero-dots{left:590px;top:383px;display:flex;gap:6px}
.hero-dots span{width:7px;height:7px;border-radius:50%;background:#777}
.hero-dots span.on{background:var(--orange)}

/* feature boxes */
.feature{top:418px;height:152px;background:#2b2b2b}
.feature-head{height:28px;border-radius:6px 6px 0 0;background:linear-gradient(#ffa04a,var(--orange) 50%,var(--orange-dark));font-size:14px;font-weight:800;font-style:italic;color:var(--white);text-transform:uppercase;padding:4px 14px;text-shadow:0 1px 1px rgba(0,0,0,.35)}
.feature-media{height:124px}
.media-video{background:linear-gradient(120deg,#eeeeee,#9d9d9d 60%,#5e5e5e)}
.media-performance{background:linear-gradient(180deg,#2a1410,#8c3418 55%,#d2601e)}
.media-athletes{background:radial-gradient(ellipse at 60% 50%,#6f6f6f,#2f2f2f 55%,#151515)}
.play{left:100px;top:42px}

/* content */
.section-title{font-size:13px;font-weight:800;color:var(--white);text-transform:uppercase;display:flex;align-items:center;gap:8px}
.section-title::before{content:"";width:6px;height:6px;background:var(--orange)}
.section-title.italic{font-style:italic}
.rule{height:1px;background:var(--line);margin:6px 0 8px}
.body-copy{font-size:8.5px;line-height:12px;color:#a9a9a9}

.about{left:240px;top:585px;width:470px}
.news{left:740px;top:585px;width:222px}
.news-item{padding-bottom:5px;margin-bottom:5px;border-bottom:1px solid var(--line)}
.news-item h4{font-size:9px;line-height:12px;font-weight:700;color:var(--orange)}
.news-item time{display:block;font-size:7.5px;line-height:10px;color:var(--muted);margin-bottom:1px}

.testimonials{left:240px;top:710px;width:220px}
.testimonials h4{font-size:9.5px;font-weight:700;color:var(--orange);text-transform:uppercase}
.testimonials time{display:block;font-size:7.5px;color:var(--muted);margin-bottom:3px}

.join{left:480px;top:710px;width:235px}
.field{display:flex;align-items:center;margin-bottom:6px}
.field label{width:72px;font-size:9px;font-weight:700;color:var(--orange);text-transform:uppercase}
.field span{flex:1;height:16px;background:#111;border:1px solid #444}
.join-actions{display:flex;align-items:center;justify-content:space-between;margin-top:4px;font-size:8px;color:#a9a9a9}
.join-actions i{display:inline-block;width:9px;height:9px;border:1px solid #777;background:#111;vertical-align:-2px;margin-right:4px}
.submit{background:var(--orange);color:var(--white);font-size:8.5px;font-weight:700;padding:3px 9px;border-radius:2px}

/* footer */
.footer{left:0;top:845px;width:1200px;height:167px;background:linear-gradient(90deg,#1a1a1a,#3e3e3e 40%,#6a6a6a)}
.footer-photo{left:760px;top:845px;width:440px;height:167px;background:linear-gradient(90deg,rgba(110,110,110,0),#8b96a3 35%,#cfd6dd 80%,#e2e6ea)}
.footer-brand{left:262px;top:893px;display:flex;align-items:center;gap:8px}
.footer-brand .brand-dot{width:26px;height:26px}
.footer-brand .brand-name{font-size:18px}
.footer-links{top:887px;font-size:10px;font-weight:700;color:var(--orange);line-height:13px;display:flex;flex-direction:column}
.copyright{left:0;top:1012px;width:1200px;height:18px;background:#0d0d0d;font-size:7.5px;color:var(--muted);padding:4px 240px}
</style>
</head>
<body>

<header>
  <div class="abs top-accent"></div>
  <div class="abs utility-links"><b>English</b> | Home | Contact | Client | Sitemap</div>
  <div class="abs brand"><span class="brand-dot"></span><span class="brand-name">TKRVantage</span></div>
  <div class="abs social" aria-label="Social links"><span></span><span></span><span></span><span></span><span></span></div>
  <div class="abs search">search
    <svg width="11" height="11" viewBox="0 0 11 11"><circle cx="4.5" cy="4.5" r="3.4" fill="none" stroke="#aaa" stroke-width="1.4"/><line x1="7" y1="7" x2="10" y2="10" stroke="#aaa" stroke-width="1.6"/></svg>
  </div>
  <nav class="abs main-nav">
    <a class="active" href="#">Home</a><a href="#">Programs</a><a href="#">Consulting</a><a href="#">Facilities</a><a href="#">Articles</a><a href="#">Store</a><a href="#">About Us</a>
  </nav>
</header>

<section class="abs hero"></section>
<div class="abs hero-photo" role="img" aria-label="Football player in uniform holding a helmet"></div>
<h1 class="abs hero-title"><span class="quote">“</span>Transforming Today's Contender<span class="line2">into <em>Tomorrow's Champion</em></span></h1>
<p class="abs hero-sub">We provide customized sport-specific programs to help you perform at your best.</p>
<svg class="abs hero-arrow" style="left:246px" width="12" height="14" viewBox="0 0 12 14"><polygon points="11,0 11,14 0,7" fill="#6d6d6d"/></svg>
<svg class="abs hero-arrow" style="left:944px" width="12" height="14" viewBox="0 0 12 14"><polygon points="1,0 1,14 12,7" fill="#6d6d6d"/></svg>
<div class="abs hero-dots"><span></span><span></span><span class="on"></span><span></span><span></span></div>

<article class="abs feature" style="left:228px;width:242px">
  <h2 class="feature-head">Video Training</h2>
  <div class="feature-media media-video" role="img" aria-label="Sprinter running on a track"></div>
  <svg class="abs play" width="36" height="36" viewBox="0 0 36 36"><circle cx="18" cy="18" r="17" fill="var(--orange)"/><polygon points="14,10 14,26 27,18" fill="#fff"/></svg>
</article>
<article class="abs feature" style="left:478px;width:244px">
  <h2 class="feature-head">Performance Training</h2>
  <div class="feature-media media-performance" role="img" aria-label="Runner crouched in the starting blocks"></div>
</article>
<article class="abs feature" style="left:730px;width:243px">
  <h2 class="feature-head">Our Athletes</h2>
  <div class="feature-media media-athletes" role="img" aria-label="Athlete portrait in dark studio light"></div>
</article>

<section class="abs about">
  <h3 class="section-title">About Us</h3>
  <div class="rule"></div>
  <p class="body-copy">Lorem ipsum dolor sit amet, consectetuer adipiscing elit, sed diam nonummy nibh euismod tincidunt ut laoreet dolore magna aliquam erat volutpat. Ut wisi enim ad minim veniam, quis nostrud exerci tation ullamcorper suscipit lobortis nisl ut aliquip ex ea commodo consequat. Duis autem vel eum iriure dolor in hendrerit in vulputate velit esse molestie consequat, vel illum dolore eu feugiat nulla facilisis at vero eros et accumsan.</p>
</section>

<section class="abs news">
  <h3 class="section-title">News</h3>
  <div class="rule"></div>
  <div class="news-item"><h4>Lorem ipsum dolor sit amet</h4><time>01/10/2012</time><p class="body-copy">Lorem ipsum dolor sit amet, consectetuer adipiscing elit, sed diam nonummy nibh.</p></div>
  <div class="news-item"><h4>Lorem ipsum dolor sit amet</h4><time>01/10/2012</time><p class="body-copy">Lorem ipsum dolor sit amet, consectetuer adipiscing elit, sed diam nonummy nibh.</p></div>
  <div class="news-item"><h4>Lorem ipsum dolor sit amet</h4><time>01/10/2012</time><p class="body-copy">Lorem ipsum dolor sit amet, consectetuer adipiscing elit, sed diam nonummy nibh.</p></div>
  <div class="news-item" style="border:0"><h4>Lorem ipsum dolor sit amet</h4><time>01/10/2012</time><p class="body-copy">Lorem ipsum dolor sit amet, consectetuer adipiscing elit, sed diam nonummy nibh.</p></div>
</section>

<section class="abs testimonials">
  <h3 class="section-title italic">Testimonials</h3>
  <div class="rule"></div>
  <h4>Athlet Name, Age</h4>
  <time>01/10/2012</time>
  <p class="body-copy">Lorem ipsum dolor sit amet, consectetuer adipiscing elit, sed diam nonummy nibh euismod tincidunt ut laoreet dolore magna aliquam erat volutpat.</p>
</section>

<section class="abs join">
  <h3 class="section-title italic">Join Us</h3>
  <div class="rule"></div>
  <div class="field"><label>Full Name:</label><span></span></div>
  <div class="field"><label>Your Phone:</label><span></span></div>
  <div class="field"><label>Your Mail:</label><span></span></div>
  <div class="join-actions"><span><i></i>Receive e-mail</span><span class="submit">SUBMIT</span></div>
</section>

<footer>
  <div class="abs footer"></div>
  <div class="abs footer-photo" role="img" aria-label="Sprinter in the set position on a track"></div>
  <div class="abs footer-brand"><span class="brand-dot"></span><span class="brand-name">TKRVantage</span></div>
  <div class="abs footer-links" style="left:450px"><a>Programs</a><a>Registration</a><a>Consulting</a></div>
  <div class="abs footer-links" style="left:560px"><a>Store</a><a>Contact Us</a><a>Links</a></div>
  <div class="abs footer-links" style="left:672px"><a>Facilities</a><a>Articles</a><a>FAQ</a></div>
  <div class="abs copyright">© 2012 TKRVantage. All Rights Reserved.</div>
</footer>

</body>
</html>
```